Flyer for corporate discount for dog daycare

I own a dog daycare with a large corporate down the road. I am working with the President of the company to offer their employees a discount for my services, Dog Daycare, Overnight Care, Grooming Salon & Spa and Retail. The design should be professional but also have a soft side as people view their dogs similar to human children.

I attached my logo along with our grooming brochure for reference on colors we've been using.

At a minimum the flyer must contain the following information:
Name: The Wagtail Lodge
web address: www.PawHavenStays.example
phone number: 920-555-0148
Address: 4872 Larchmont Lane
Google Map of our location

Title of flyer/program: Corporate V.I.P. (Very Important Pooch) (Can be creative with how to include this such as, Welcome to our Corporate. . .. etc.)

The program offer is: 5% discount
My services: Dog Daycare, Overnight Care, Grooming Salon & Spa and Retail

Target Market(s)

corporate employees, male and female, age 24+

Industry/Entity Type

Daycare

Requirements
Must have
• Must be easy to read and inviting.
Nice to have
• Nice photo dogs playing or inviting photo of dog.
Should not have
• cartoon feel

```html
<!DOCTYPE html>
<html lang="en">
<head>
<meta charset="utf-8">
<title>The Wagtail Lodge – Corporate V.I.P. Discount Flyer</title>
<link rel="stylesheet" href="https://fonts.googleapis.com/css2?family=Roboto+Condensed:wght@700&family=Great+Vibes&family=Cabin:wght@400;600&display=swap">
<style>
  :root {
    --white: #ffffff;
    --brand-blue: #1ba1e2;
    --sky: #08a9ea;
    --pale-blue: #ade0e8;
    --lime: #a9cd3a;
    --earth: #4b4231;
    --olive-ink: #4a4630;
    --body-ink: #2b2a1c;
    --alert-red: #e8222a;
    --map-green: #cfe3b4;
    --map-road: #f4f1e6;
  }
  html, body {
    margin: 0;
    padding: 0;
    width: 975px;
    height: 1200px;
    overflow: hidden;
    background: var(--white);
  }
  .flyer {
    position: relative;
    width: 975px;
    height: 1200px;
    overflow: hidden;
    background: var(--white);
    font-family: "Cabin", sans-serif;
  }
  .backdrop {
    position: absolute;
    inset: 0;
  }
  .top-url {
    position: absolute;
    left: 58px;
    top: 40px;
    margin: 0;
    font-family: "Roboto Condensed", sans-serif;
    font-weight: 700;
    font-size: 30px;
    letter-spacing: 0.5px;
    color: var(--brand-blue);
  }
  .brand {
    position: absolute;
    left: 680px;
    top: 40px;
    width: 260px;
  }
  .brand-square {
    width: 130px;
    height: 130px;
    background: var(--pale-blue);
  }
  .brand-name {
    margin: 12px 0 0;
    font-family: "Roboto Condensed", sans-serif;
    font-weight: 700;
    font-size: 30px;
    color: var(--earth);
    white-space: nowrap;
  }
  .welcome {
    position: absolute;
    left: 56px;
    top: 222px;
    margin: 0;
    font-family: "Great Vibes", cursive;
    font-weight: 400;
    font-size: 54px;
    line-height: 70px;
    color: var(--white);
    white-space: nowrap;
  }
  .headline {
    position: absolute;
    left: 50px;
    top: 300px;
    margin: 0;
    font-family: "Roboto Condensed", sans-serif;
    font-weight: 700;
    font-size: 50px;
    line-height: 58px;
    color: var(--white);
    white-space: nowrap;
  }
  .program {
    position: absolute;
    left: 52px;
    top: 362px;
    margin: 0;
    font-weight: 600;
    font-size: 17px;
    letter-spacing: 0.3px;
    color: var(--olive-ink);
    white-space: nowrap;
  }
  .services {
    position: absolute;
    left: 60px;
    top: 432px;
    margin: 0;
    padding: 0;
    list-style: none;
  }
  .services li {
    display: flex;
    align-items: center;
    height: 49px;
    font-family: "Roboto Condensed", sans-serif;
    font-weight: 700;
    font-size: 35px;
    color: var(--olive-ink);
  }
  .services svg {
    width: 26px;
    height: 26px;
    margin-right: 16px;
    flex: none;
  }
  .benefits-title {
    position: absolute;
    left: 60px;
    top: 650px;
    margin: 0;
    font-weight: 600;
    font-size: 21px;
    color: var(--white);
  }
  .benefits {
    position: absolute;
    left: 60px;
    top: 688px;
    width: 400px;
    margin: 0;
    padding: 0;
    list-style: none;
    font-size: 16.5px;
    line-height: 22px;
    color: var(--body-ink);
  }
  .benefits li {
    position: relative;
    padding-left: 17px;
    margin-bottom: 3.5px;
  }
  .benefits li::before {
    content: "";
    position: absolute;
    left: 1px;
    top: 6px;
    width: 10px;
    height: 10px;
    border-radius: 50%;
    background: var(--alert-red);
  }
  .hero-photo {
    position: absolute;
    left: 470px;
    top: 300px;
    width: 505px;
    height: 722px;
    border-radius: 250px 0 0 40px;
    background: linear-gradient(160deg, #7a4a2e 0%, #e9d9c0 35%, #f1e7d6 55%, #e8789a 100%);
  }
  .pets-photo {
    position: absolute;
    left: 36px;
    top: 840px;
    width: 424px;
    height: 140px;
    border-radius: 60px 60px 0 0;
    background: linear-gradient(90deg, #1c1c1c 0%, #e8e2da 25%, #222 45%, #f2efe9 65%, #151515 100%);
  }
  .offer {
    position: absolute;
    left: 43px;
    top: 967px;
    width: 418px;
    height: 192px;
    border-radius: 12px;
    background: var(--alert-red);
    box-shadow: 0 6px 0 rgba(0, 0, 0, 0.18);
    color: var(--white);
    text-align: center;
  }
  .offer-title {
    margin: 36px 0 0;
    font-family: "Roboto Condensed", sans-serif;
    font-weight: 700;
    font-size: 58px;
    line-height: 60px;
  }
  .offer-url {
    margin: 12px 0 0;
    font-family: "Roboto Condensed", sans-serif;
    font-weight: 700;
    font-size: 27px;
  }
  .offer-address {
    margin: 10px 0 0;
    font-size: 18px;
  }
  .location-map {
    position: absolute;
    left: 482px;
    top: 1082px;
    width: 104px;
    height: 96px;
    border: 3px solid var(--white);
    border-radius: 6px;
    overflow: hidden;
    background: var(--map-green);
  }
  .location-map svg {
    display: block;
  }
  .phone {
    position: absolute;
    left: 602px;
    top: 1112px;
    margin: 0;
    font-family: "Roboto Condensed", sans-serif;
    font-weight: 700;
    font-size: 54px;
    color: var(--white);
    text-shadow: 0 2px 3px rgba(0, 0, 0, 0.25);
  }
</style>
</head>
<body>
<main class="flyer">
  <svg class="backdrop" width="975" height="1200" viewBox="0 0 975 1200" aria-hidden="true">
    <rect x="0" y="820" width="975" height="380" fill="var(--sky)"/>
    <path d="M0,112 C250,60 560,140 760,330 C900,470 975,560 975,700 L975,900 C975,1040 760,1110 480,1108 C300,1106 120,1060 0,1000 Z" fill="var(--earth)"/>
    <path d="M0,134 C250,92 540,160 740,348 C880,480 950,580 950,720 L950,880 C950,1010 760,1072 500,1072 C310,1072 130,1022 0,960 Z" fill="var(--pale-blue)"/>
    <path d="M0,200 C260,142 520,192 720,372 C860,500 925,600 925,730 L925,860 C925,990 760,1040 520,1040 C330,1040 140,990 0,900 Z" fill="var(--lime)"/>
  </svg>

  <p class="top-url">www.PawHavenStays.example</p>

  <div class="brand">
    <div class="brand-square"></div>
    <p class="brand-name">THE WAGTAIL LODGE</p>
  </div>

  <p class="welcome">Inviting Our V.I.P.s to</p>
  <h1 class="headline">THE WAGTAIL LODGE</h1>
  <p class="program">CORPORATE V.I.P. · Very Important Pooch Program</p>

  <ul class="services">
    <li><svg viewBox="0 0 26 26"><rect x="2" y="5" width="19" height="19" fill="none" stroke="var(--white)" stroke-width="2.5"/><path d="M6 13 L11 19 L23 3" fill="none" stroke="var(--white)" stroke-width="3"/></svg>DOG DAYCARE</li>
    <li><svg viewBox="0 0 26 26"><rect x="2" y="5" width="19" height="19" fill="none" stroke="var(--white)" stroke-width="2.5"/><path d="M6 13 L11 19 L23 3" fill="none" stroke="var(--white)" stroke-width="3"/></svg>OVERNIGHT CARE</li>
    <li><svg viewBox="0 0 26 26"><rect x="2" y="5" width="19" height="19" fill="none" stroke="var(--white)" stroke-width="2.5"/><path d="M6 13 L11 19 L23 3" fill="none" stroke="var(--white)" stroke-width="3"/></svg>GROOMING SALON</li>
    <li><svg viewBox="0 0 26 26"><rect x="2" y="5" width="19" height="19" fill="none" stroke="var(--white)" stroke-width="2.5"/><path d="M6 13 L11 19 L23 3" fill="none" stroke="var(--white)" stroke-width="3"/></svg>SPA AND RETAIL</li>
  </ul>

  <h2 class="benefits-title">Benefits of Dog Daycare</h2>
  <ul class="benefits">
    <li>Provides physical activity, exercise and stimulation</li>
    <li>Increased social skills</li>
    <li>Decreased destructive behaviors due to boredom</li>
    <li>Builds confidence in timid or fearful dogs</li>
    <li>Offers a safe and controlled environment for appropriate play</li>
  </ul>

  <div class="hero-photo" role="img" aria-label="Photo of a smiling woman in a pink top hugging a cream-coloured Labrador puppy"></div>

  <div class="pets-photo" role="img" aria-label="Photo of a row of sitting dogs and cats of various breeds"></div>

  <section class="offer">
    <p class="offer-title">5% DISCOUNT</p>
    <p class="offer-url">www.PawHavenStays.example</p>
    <p class="offer-address">4872 Larchmont Lane Millbrook, WI 54900</p>
  </section>

  <div class="location-map" role="img" aria-label="Map showing the location of The Wagtail Lodge at 4872 Larchmont Lane">
    <svg width="104" height="96" viewBox="0 0 104 96" aria-hidden="true">
      <path d="M52 30 C43 30 37 37 37 45 C37 56 52 70 52 70 C52 70 67 56 67 45 C67 37 61 30 52 30 Z" fill="var(--alert-red)"/>
      <circle cx="52" cy="45" r="5" fill="var(--white)"/>
    </svg>
  </div>

  <p class="phone">920.555.0148</p>
</main>
</body>
</html>
```